Business Card Design

We sell fish products to corporate food companies who then turn these products into final food products for consumers

Industry/Entity Type

Business

Contact Information for Business Card

I need a corporate business card template for a fish products business. We would like it be professional for use in dealing with multi national companies. This company business card template will be used by multiple employees so the following fields must be open to edit (Name, Phone Number and Email address)

```html
<!DOCTYPE html>
<html lang="en">
<head>
<meta charset="UTF-8">
<title>Tidewater Catch – Business Card</title>
<link href="https://fonts.googleapis.com/css2?family=Open+Sans:wght@400;600&display=swap" rel="stylesheet">
<style>
  :root {
    --backdrop: #e9e6e1;
    --card: #fbfbfb;
    --brand-blue: #1d5fb4;
    --ink: #3a3a3a;
    --icon-grey: #555a60;
  }
  html, body {
    margin: 0;
    padding: 0;
    width: 1200px;
    height: 800px;
    overflow: hidden;
    background: var(--backdrop);
    font-family: "Open Sans", Arial, sans-serif;
  }
  .business-card {
    position: absolute;
    left: 100px;
    top: 114px;
    width: 1000px;
    height: 572px;
    background: var(--card);
    box-shadow: 0 6px 24px rgba(0,0,0,0.12);
  }
  .brand {
    position: absolute;
    left: 60px;
    top: 170px;
    width: 400px;
    text-align: center;
  }
  .brand-mark {
    width: 90px;
    height: 90px;
    border-radius: 50%;
    background: var(--brand-blue);
    margin: 0 auto 22px;
  }
  .brand-name {
    margin: 0;
    color: var(--brand-blue);
    font-weight: 600;
    font-size: 44px;
    line-height: 1.1;
    letter-spacing: 1px;
    text-transform: uppercase;
  }
  .contact-line {
    position: absolute;
    inset: 0;
  }
  .contact-item {
    position: absolute;
    margin: 0;
    color: var(--ink);
    font-weight: 400;
    white-space: nowrap;
  }
  .contact-name { left: 562px; top: 172px; font-size: 29px; }
  .contact-phone { left: 574px; top: 258px; font-size: 24px; }
  .contact-email { left: 560px; top: 340px; font-size: 24px; }
</style>
</head>
<body>
  <main class="business-card">
    <div class="brand">
      <div class="brand-mark"></div>
      <p class="brand-name">Tidewater<br>Catch</p>
    </div>

    <svg class="contact-line" width="1000" height="572" viewBox="0 0 1000 572" aria-hidden="true">
      <path d="M445 67 Q600 275 435 480" fill="none" stroke="var(--brand-blue)" stroke-width="3"/>
      <circle cx="445" cy="67" r="6" fill="var(--brand-blue)"/>
      <circle cx="435" cy="480" r="6" fill="var(--brand-blue)"/>

      <g class="icon-person">
        <circle cx="509" cy="192" r="25" fill="var(--card)" stroke="var(--brand-blue)" stroke-width="3"/>
        <circle cx="509" cy="185" r="6" fill="var(--icon-grey)"/>
        <path d="M497 203 Q497 193 509 193 Q521 193 521 203 Z" fill="var(--icon-grey)"/>
      </g>

      <g class="icon-phone">
        <circle cx="520" cy="274" r="25" fill="var(--card)" stroke="var(--brand-blue)" stroke-width="3"/>
        <path d="M511 263 L516 262 L519 269 L516 272 Q519 279 524 282 L527 279 L534 282 L533 287 Q531 290 527 289 Q513 284 508 270 Q507 265 511 263 Z" fill="var(--icon-grey)"/>
      </g>

      <g class="icon-mail">
        <circle cx="505" cy="357" r="25" fill="var(--card)" stroke="var(--brand-blue)" stroke-width="3"/>
        <rect x="493" y="349" width="24" height="17" rx="2" fill="var(--icon-grey)"/>
        <path d="M494 351 L505 359 L516 351" fill="none" stroke="var(--card)" stroke-width="2"/>
      </g>
    </svg>

    <p class="contact-item contact-name">Mara Ellwood</p>
    <p class="contact-item contact-phone">321-555-014</p>
    <p class="contact-item contact-email">hello@tidewatercatch.com</p>
  </main>
</body>
</html>
```